BUSINESS CARDS, ENVELOPE, LETTER HEADS AND OTHER STATIONARY
FOR BROOKFERN DATA TECHNOLOGY
I need double sided standard sized Business Card [3.5" x 2"]
Please show me a wide variey of fonts including the ones from the logo
Bright & Fun-filled
Dorian Velmont
Solutions Architect / Technical Sales
82 Pinewhistle Crescent SW
Calgary, Alberta
Canada T2K7M5
dorianv@brookferndataworks.example
http://www.brookferndataworks.example
On the Back of the Bussiness Card I would like to describe a few of the features and solutions that Brookfern Data provides like:
- Electronic Records Management
-IT Solutions (Hardware / Software)
- After hours Technical support (Disaster Recover)
- Procurement
Logo
LOGO file 2
Please Do Not Include the Reflection as part of the logo Thank You

```html
<!DOCTYPE html>
<html lang="en">
<head>
<meta charset="utf-8">
<title>Brookfern Data – Stationery</title>
<link href="https://fonts.googleapis.com/css2?family=Open+Sans:wght@400;700&display=swap" rel="stylesheet">
<style>
:root{
  --blue:#1a5cae;
  --navy:#163c7e;
  --green:#5aae2e;
  --lime:#8cc63f;
  --ink:#2f3b4a;
  --paper:#ffffff;
  --ground:#eee8e0;
  --faint:#eef0f2;
}
*{box-sizing:border-box;margin:0;padding:0}
html,body{width:1200px;height:497px;overflow:hidden;background:var(--ground);font-family:"Open Sans",Arial,sans-serif;color:var(--ink)}
.canvas{position:relative;width:1200px;height:497px}
.piece{position:absolute;background:var(--paper);box-shadow:0 2px 6px rgba(0,0,0,.18);overflow:hidden}
.piece svg.shape{position:absolute;inset:0;width:100%;height:100%}
.brand{position:absolute;display:flex;align-items:center;gap:5px}
.brand.stacked{flex-direction:column;align-items:flex-start;gap:3px}
.brand .dot{border-radius:50%;background:var(--blue)}
.brand .name{font-weight:700;color:var(--navy);white-space:nowrap;line-height:1}
.contact{position:absolute;font-size:5px;line-height:1.45;color:var(--ink);white-space:nowrap}
.contact.compact{font-size:4.4px}
.contact .who{font-weight:700;font-size:6px;color:var(--navy)}
.contact .role{color:var(--green);font-size:4.5px;margin-bottom:3px}
.services{position:absolute;list-style:none;font-size:5.2px;line-height:1.9;color:#fff;white-space:nowrap}
.services li::before{content:"";display:inline-block;width:3px;height:3px;border-radius:50%;background:#fff;margin-right:4px;vertical-align:middle}
.services.dark{color:var(--navy)}
.services.dark li::before{background:var(--green)}
.card{width:180px;height:106px}
.card.back-blue{background:linear-gradient(135deg,var(--navy),var(--blue) 60%,#3d86cf)}
.card.back-green{background:linear-gradient(135deg,#3f8f25,var(--green) 60%,var(--lime))}
.watermark{position:absolute;border-radius:50%;background:var(--faint)}
.addr{position:absolute;font-size:4.4px;line-height:1.5;color:var(--ink);white-space:nowrap}
</style>
</head>
<body>
<main class="canvas">

  <!-- Business card fronts -->
  <section class="piece card" style="left:24px;top:72px">
    <svg class="shape" viewBox="0 0 180 106" preserveAspectRatio="none"><defs><linearGradient id="sw1" x1="0" y1="0" x2="1" y2="1"><stop offset="0" stop-color="#163c7e"/><stop offset=".6" stop-color="#1a5cae"/><stop offset="1" stop-color="#5aae2e"/></linearGradient></defs><path d="M0 0H46C30 10 20 40 18 106H0Z" fill="url(#sw1)"/></svg>
    <div class="brand" style="left:28px;top:10px"><span class="dot" style="width:16px;height:16px"></span><span class="name" style="font-size:8px">Brookfern Data</span></div>
    <div class="contact" style="left:34px;top:52px"><div class="who">Dorian Velmont</div><div class="role">Solutions Architect / Technical Sales</div></div>
  </section>

  <section class="piece card" style="left:221px;top:72px">
    <svg class="shape" viewBox="0 0 180 106" preserveAspectRatio="none"><defs><linearGradient id="sw2" x1="0" y1="0" x2="1" y2="1"><stop offset="0" stop-color="#163c7e"/><stop offset=".6" stop-color="#1a5cae"/><stop offset="1" stop-color="#5aae2e"/></linearGradient></defs><path d="M0 60C20 70 30 90 34 106H0Z" fill="url(#sw2)"/></svg>
    <div class="brand stacked" style="left:10px;top:10px"><span class="dot" style="width:14px;height:14px"></span><span class="name" style="font-size:6px">Brookfern Data</span></div>
    <div class="contact compact" style="left:80px;top:10px">
      <div class="who">Dorian Velmont</div>
      <div class="role">Solutions Architect / Technical Sales</div>
      82 Pinewhistle Crescent SW<br>Calgary, Alberta<br>Canada T2K7M5<br>
      T 403.555.0147<br>C 403.555.0196<br>
      dorianv@brookferndataworks.example<br>http://www.brookferndataworks.example
    </div>
  </section>

  <!-- Business card backs -->
  <section class="piece card back-blue" style="left:24px;top:197px">
    <div class="watermark" style="left:110px;top:30px;width:70px;height:70px;opacity:.12"></div>
    <ul class="services" style="left:12px;top:22px">
      <li>Electronic Records Management</li>
      <li>IT Solutions (Hardware / Software)</li>
      <li>After hours Technical support (Disaster Recover)</li>
      <li>Procurement</li>
    </ul>
  </section>

  <section class="piece card back-green" style="left:221px;top:197px">
    <div class="watermark" style="left:110px;top:30px;width:70px;height:70px;opacity:.14"></div>
    <ul class="services" style="left:12px;top:22px">
      <li>Electronic Records Management</li>
      <li>IT Solutions (Hardware / Software)</li>
      <li>After hours Technical support (Disaster Recover)</li>
      <li>Procurement</li>
    </ul>
  </section>

  <section class="piece card" style="left:120px;top:316px;height:108px">
    <div class="brand" style="left:12px;top:12px"><span class="dot" style="width:18px;height:18px"></span><span class="name" style="font-size:8px">Brookfern Data</span></div>
    <ul class="services dark" style="left:12px;top:42px">
      <li>Electronic Records Management</li>
      <li>IT Solutions (Hardware / Software)</li>
      <li>After hours Technical support (Disaster Recover)</li>
      <li>Procurement</li>
    </ul>
  </section>

  <!-- Letterhead -->
  <section class="piece" style="left:432px;top:26px;width:230px;height:316px">
    <svg class="shape" viewBox="0 0 230 316" preserveAspectRatio="none"><defs><linearGradient id="lh" x1="0" y1="0" x2="1" y2="0"><stop offset="0" stop-color="#163c7e"/><stop offset=".5" stop-color="#1a5cae"/><stop offset="1" stop-color="#5aae2e"/></linearGradient></defs><path d="M0 0H70C40 4 20 14 0 30Z" fill="url(#lh)"/><path d="M230 290C200 300 180 310 170 316H230Z" fill="url(#lh)"/></svg>
    <div class="brand" style="left:14px;top:14px"><span class="dot" style="width:18px;height:18px"></span><span class="name" style="font-size:9px">Brookfern Data</span></div>
    <div class="addr" style="left:140px;top:14px">82 Pinewhistle Crescent SW<br>Calgary, Alberta<br>Canada T2K7M5<br>dorianv@brookferndataworks.example<br>http://www.brookferndataworks.example</div>
    <div class="watermark" style="left:55px;top:100px;width:120px;height:120px"></div>
  </section>

  <!-- Envelope backs -->
  <section class="piece" style="left:724px;top:28px;width:334px;height:150px">
    <svg class="shape" viewBox="0 0 334 150" preserveAspectRatio="none"><defs><linearGradient id="fl1" x1="0" y1="0" x2="1" y2="0"><stop offset="0" stop-color="#3f8f25"/><stop offset=".5" stop-color="#5aae2e"/><stop offset="1" stop-color="#3f8f25"/></linearGradient></defs><rect width="334" height="150" fill="url(#fl1)"/><path d="M0 150L167 60L334 150Z" fill="#4a9a2a"/></svg>
    <div class="brand" style="left:155px;top:8px"><span class="dot" style="width:24px;height:24px"></span></div>
  </section>

  <section class="piece" style="left:724px;top:130px;width:334px;height:120px">
    <svg class="shape" viewBox="0 0 334 120" preserveAspectRatio="none"><path d="M0 0H334L167 70Z" fill="#f3f4f6"/><path d="M0 0L167 70L334 0" fill="none" stroke="#d8dde2" stroke-width="1"/></svg>
    <div class="brand" style="left:155px;top:50px"><span class="dot" style="width:22px;height:22px"></span></div>
  </section>

  <!-- Envelope front -->
  <section class="piece" style="left:668px;top:228px;width:270px;height:192px">
    <svg class="shape" viewBox="0 0 270 192" preserveAspectRatio="none"><defs><linearGradient id="ef" x1="0" y1="0" x2="1" y2="0"><stop offset="0" stop-color="#163c7e"/><stop offset=".55" stop-color="#1a5cae"/><stop offset="1" stop-color="#5aae2e"/></linearGradient></defs><path d="M0 0H270V20C190 6 90 10 0 40Z" fill="url(#ef)"/></svg>
    <div class="brand" style="left:12px;top:40px"><span class="dot" style="width:20px;height:20px"></span><span class="name" style="font-size:9px">Brookfern Data</span></div>
    <div class="addr" style="left:14px;top:130px">82 Pinewhistle Crescent SW<br>Calgary, Alberta<br>Canada T2K7M5<br>dorianv@brookferndataworks.example<br>http://www.brookferndataworks.example</div>
    <div class="watermark" style="left:150px;top:70px;width:100px;height:100px"></div>
  </section>

</main>
</body>
</html>
```